social interest sharing site needs a web site design

we need a web site design for a social web platform.
the site is one page(main page), that is split into 3 sections
each section is a different color(red,green and blue)
and a user can choose to share each of the sections.
any section/color will contain boxes , each box can contain different media types.

the media types:
* list of URLS
* list of articles including title + image + description
* list of videos
* thumbnails of images
* calender
* list of emails

the main content will look like quiltboard layout
multiple boxes each box can contain different type of content as described above

each color is a different tab
each tab will have layout like quiltboard
Updates

please read the last description update.
and i uploaded an image that can explain the requirements better

thanks
Oren

```html
<!DOCTYPE html>
<html lang="en">
<head>
<meta charset="utf-8">
<title>tricolour. – share by colour</title>
<link rel="stylesheet" href="https://fonts.googleapis.com/css2?family=Varela+Round&family=Sriracha&display=swap">
<style>
:root{
  --ink:#3a3a3a;
  --paper:#ffffff;
  --faint:#efebe8;
  --red:#f47777;
  --red-deep:#e06767;
  --green:#4fddc3;
  --green-deep:#3fcdb3;
  --blue:#455c87;
  --blue-deep:#3b5079;
  --chip:rgba(255,255,255,.22);
  --cell:#ffffff;
}
*{box-sizing:border-box;margin:0;padding:0}
html,body{width:1200px;height:754px;overflow:hidden;background:var(--paper);font-family:"Varela Round",sans-serif;color:var(--ink)}
.page{position:relative;width:1200px;height:754px}
.masthead{position:absolute;left:0;top:0;width:1200px;height:136px;background:var(--paper)}
.brand{position:absolute;left:0;width:1200px;top:8px;text-align:center;font-size:58px;font-weight:700;letter-spacing:-1px;color:var(--ink);font-family:"Varela Round",sans-serif}
.share-row{position:absolute;display:flex;gap:8px}
.masthead .share-row{left:422px;top:76px}
.chip{width:44px;height:44px;border-radius:50%;background:var(--faint);display:flex;align-items:center;justify-content:center;font-size:11px;color:var(--paper);font-family:"Varela Round",sans-serif}
.mail{position:absolute;left:1098px;top:65px}
.column{position:absolute;top:136px;height:618px;overflow:hidden}
.column::before{content:"";position:absolute;left:0;top:0;width:100%;height:12px}
.col-red{left:0;width:400px;background:var(--red)}
.col-red::before{background:var(--red-deep)}
.col-green{left:400px;width:399px;background:var(--green)}
.col-green::before{background:var(--green-deep)}
.col-blue{left:799px;width:401px;background:var(--blue)}
.col-blue::before{background:var(--blue-deep)}
.column .share-row{top:28px;left:22px}
.column .chip{background:var(--chip)}
.chip.active{background:var(--paper);color:var(--red)}
.scrollbar{position:absolute;left:384px;top:24px;width:14px;height:600px;background:var(--red-deep);border-radius:7px}
.scrollbar span{position:absolute;left:0;top:0;width:14px;height:28px;background:var(--paper);border-radius:7px}
.kind{position:absolute;width:22px;height:22px}
.box{position:absolute}
.fill{position:absolute}
.grid{display:grid}
.card{background:var(--paper);text-align:center;overflow:hidden}
.grass-title{font-size:18px;font-weight:700;margin-top:6px;color:var(--ink)}
.grass-sub{font-size:10px;line-height:13px;color:var(--ink)}
.url-list{list-style:none;padding:10px 0 0 26px;background:var(--paper)}
.url-list li{font-size:16px;line-height:31px;font-weight:700;color:var(--ink);position:relative}
.url-list li::before{content:"";position:absolute;left:-4px;top:12px;width:3px;height:3px;border-radius:50%;background:var(--green)}
.calendar{display:grid;grid-template-columns:repeat(7,1fr);gap:2px}
.calendar i{display:block;height:22px;background:var(--cell)}
.headline{font-weight:700;color:var(--ink);line-height:1}
.hl-small{font-size:31px;margin-top:22px}
.hl-big{font-size:58px;margin-top:4px;letter-spacing:1px}
.hl-script{font-family:"Sriracha",cursive;font-size:28px;margin-top:2px}
.mail-list{background:var(--paper);padding:8px 0 0 18px;font-size:17px;font-weight:700;height:200px}
</style>
</head>
<body>
<div class="page">
  <header class="masthead">
    <div class="brand">tricolour.</div>
    <div class="share-row">
      <div class="chip">Ping</div><div class="chip">Chirp</div><div class="chip">Link</div><div class="chip">Feed</div><div class="chip">Loop</div><div class="chip">Vote</div><div class="chip">Yell</div>
    </div>
    <svg class="mail" width="82" height="54" viewBox="0 0 82 54" aria-label="Contact">
      <rect x="0" y="0" width="82" height="54" rx="3" fill="var(--faint)"/>
      <path d="M6 4 L41 46 L76 4" fill="none" stroke="var(--paper)" stroke-width="4"/>
    </svg>
  </header>

  <!-- red section -->
  <section class="column col-red">
    <div class="share-row">
      <div class="chip active">Ping</div><div class="chip">Chirp</div><div class="chip">Link</div><div class="chip">Feed</div><div class="chip">Loop</div><div class="chip">Vote</div><div class="chip">Yell</div>
    </div>
    <div class="scrollbar"><span></span></div>

    <svg class="kind" style="left:19px;top:106px" viewBox="0 0 22 22"><rect x="1" y="1" width="20" height="20" fill="none" stroke="#fff" stroke-width="1.5"/><path d="M3 18 L9 10 L13 15 L16 12 L19 18Z" fill="#fff"/><circle cx="8" cy="6" r="2" fill="#fff"/></svg>
    <div class="box grid" style="left:18px;top:121px;width:363px;height:137px;grid-template-columns:repeat(5,1fr)" role="img" aria-label="Thumbnail gallery of nature photos">
      <div style="background:linear-gradient(#6e8a4a,#c8576c)"></div><div style="background:linear-gradient(135deg,#1b2a5a,#3d63a8)"></div><div style="background:linear-gradient(#a9c4c2,#d8d2bd)"></div><div style="background:linear-gradient(#b5a36a,#6d6137)"></div><div style="background:linear-gradient(#c29860,#7a5430)"></div>
      <div style="background:linear-gradient(#93a15e,#6f7d3c)"></div><div style="background:linear-gradient(#c3c9cf,#8a939a)"></div><div style="background:linear-gradient(#8ea3ae,#6b7a55)"></div><div style="background:linear-gradient(#d8c7a3,#a8895a)"></div><div style="background:linear-gradient(#4c5a94,#8c97c8)"></div>
    </div>

    <svg class="kind" style="left:19px;top:278px" viewBox="0 0 22 22"><rect x="1" y="1" width="20" height="20" fill="none" stroke="#fff" stroke-width="1.5"/><path d="M5 6h12M5 10h12M5 14h12M5 18h12" stroke="#fff" stroke-width="1.5"/></svg>
    <div class="box card" style="left:18px;top:300px;width:174px;height:137px">
      <div style="height:80px;background:linear-gradient(#3c3c3c,#bdbdbd)" role="img" aria-label="Black and white photo of grass stalks"></div>
      <div class="grass-title">GRASS:</div>
      <div class="grass-sub">DANGEROUS DRUG,<br>OR NATURES CARPET?</div>
    </div>
    <svg class="kind" style="left:208px;top:278px" viewBox="0 0 22 22"><rect x="1" y="1" width="20" height="20" fill="none" stroke="#fff" stroke-width="1.5"/><path d="M3 18 L9 10 L13 15 L16 12 L19 18Z" fill="#fff"/><circle cx="8" cy="6" r="2" fill="#fff"/></svg>
    <div class="box" style="left:206px;top:300px;width:174px;height:137px;background:linear-gradient(#e8a9d8,#b582c4 60%,#a97bbb)" role="img" aria-label="Misty purple forest photo"></div>

    <svg class="kind" style="left:19px;top:455px" viewBox="0 0 22 22"><rect x="1" y="3" width="20" height="16" fill="none" stroke="#fff" stroke-width="1.5"/><path d="M1 7h20M1 15h20" stroke="#fff" stroke-width="1.5"/></svg>
    <div class="box" style="left:18px;top:476px;width:362px;height:142px;background:linear-gradient(#1e5f6b,#2a8a78)" role="img" aria-label="Video of a flower"></div>
  </section>

  <!-- green section -->
  <section class="column col-green">
    <div class="share-row">
      <div class="chip">Ping</div><div class="chip">Chirp</div><div class="chip">Link</div><div class="chip">Feed</div><div class="chip">Loop</div><div class="chip">Vote</div><div class="chip">Yell</div>
    </div>
    <svg class="kind" style="left:20px;top:106px" viewBox="0 0 22 22"><rect x="1" y="3" width="20" height="16" fill="none" stroke="#fff" stroke-width="1.5"/><path d="M1 7h20M1 15h20" stroke="#fff" stroke-width="1.5"/></svg>
    <div class="box" style="left:18px;top:121px;width:174px;height:137px;background:linear-gradient(#3a3330,#6b6660)" role="img" aria-label="Video of a person talking to camera">
      <svg style="position:absolute;left:65px;top:48px" width="50" height="34" viewBox="0 0 50 34"><rect width="50" height="34" rx="8" fill="#222" opacity=".85"/><path d="M20 10 L32 17 L20 24Z" fill="#fff"/></svg>
    </div>
    <svg class="kind" style="left:20px;top:278px" viewBox="0 0 22 22"><rect x="1" y="2" width="20" height="18" fill="none" stroke="#fff" stroke-width="1.5"/><path d="M1 7h20" stroke="#fff" stroke-width="1.5"/><path d="M4 11l1.5 5 1.5-4 1.5 4 1.5-5M10 11l1.5 5 1.5-4 1.5 4 1.5-5" stroke="#fff" fill="none"/></svg>
    <ul class="box url-list" style="left:19px;top:300px;width:173px;height:330px">
      <li>leafio.com</li><li>leafcity.com</li><li>leaftown.org</li><li>leafio.com</li><li>leafcity.com</li><li>leaftown.org</li>
    </ul>

    <svg class="kind" style="left:208px;top:106px" viewBox="0 0 22 22"><rect x="1" y="1" width="20" height="20" fill="none" stroke="#fff" stroke-width="1.5"/><path d="M3 18 L9 10 L13 15 L16 12 L19 18Z" fill="#fff"/><circle cx="8" cy="6" r="2" fill="#fff"/></svg>
    <div class="box grid" style="left:207px;top:121px;width:173px;height:316px;grid-template-columns:1fr 1fr;grid-template-rows:56px 87px 88px 85px" role="img" aria-label="Thumbnail gallery of landscape photos">
      <div style="background:linear-gradient(#a4ad7b,#6f7d46)"></div><div style="background:linear-gradient(#b9bcbe,#8b9297)"></div>
      <div style="background:linear-gradient(#7f9b7d,#4f7a56)"></div><div style="background:linear-gradient(#c9c2b3,#8c8f7a)"></div>
      <div style="background:linear-gradient(#c9a373,#8e6a3d)"></div><div style="background:linear-gradient(#e9a4c3,#6c5ea7)"></div>
      <div style="background:linear-gradient(#4e8f2e,#2a6a1c)"></div><div style="background:linear-gradient(#5c7dc3,#b6c8ec)"></div>
    </div>

    <svg class="kind" style="left:208px;top:455px" viewBox="0 0 22 22"><rect x="1" y="3" width="20" height="18" fill="none" stroke="#fff" stroke-width="1.5"/><path d="M1 8h20M6 1v4M16 1v4M10 11h2v7" stroke="#fff" stroke-width="1.5" fill="none"/></svg>
    <div class="box calendar" style="left:209px;top:476px;width:171px">
      <i></i><i></i><i></i><i></i><i></i><i></i><i></i>
      <i></i><i></i><i></i><i></i><i></i><i></i><i></i>
      <i></i><i></i><i></i><i></i><i></i><i></i><i></i>
      <i></i><i></i><i></i><i></i><i></i><i></i><i></i>
      <i></i><i></i><i></i><i></i><i></i><i></i><i></i>
    </div>
  </section>

  <!-- blue section -->
  <section class="column col-blue">
    <div class="share-row" style="left:23px">
      <div class="chip">Ping</div><div class="chip">Chirp</div><div class="chip">Link</div><div class="chip">Feed</div><div class="chip">Loop</div><div class="chip">Vote</div><div class="chip">Yell</div>
    </div>
    <svg class="kind" style="left:22px;top:106px" viewBox="0 0 22 22"><rect x="1" y="1" width="20" height="20" fill="none" stroke="#fff" stroke-width="1.5"/><path d="M5 6h12M5 10h12M5 14h12M5 18h12" stroke="#fff" stroke-width="1.5"/></svg>
    <article class="box card" style="left:19px;top:121px;width:364px;height:316px">
      <div style="height:166px;background:radial-gradient(circle at 45% 55%,#e45c8e 0 22%,#8bab55 45%,#a8c07a)" role="img" aria-label="Photo of pink poppy flowers"></div>
      <div class="headline hl-small">HOW TO EAT</div>
      <div class="headline hl-big">FLOWERS</div>
      <div class="headline hl-script">like a boss</div>
    </article>

    <svg class="kind" style="left:22px;top:455px" viewBox="0 0 22 22"><rect x="1" y="3" width="20" height="18" fill="none" stroke="#fff" stroke-width="1.5"/><path d="M1 8h20M6 1v4M16 1v4M10 11h2v7" stroke="#fff" stroke-width="1.5" fill="none"/></svg>
    <div class="box calendar" style="left:21px;top:476px;width:172px">
      <i></i><i></i><i></i><i></i><i></i><i></i><i></i>
      <i></i><i></i><i></i><i></i><i></i><i></i><i></i>
      <i></i><i></i><i></i><i></i><i></i><i></i><i></i>
      <i></i><i></i><i></i><i></i><i></i><i></i><i></i>
      <i></i><i></i><i></i><i></i><i></i><i></i><i></i>
    </div>
    <svg class="kind" style="left:209px;top:455px" viewBox="0 0 22 22"><rect x="1" y="1" width="20" height="20" fill="none" stroke="#fff" stroke-width="1.5"/><circle cx="11" cy="11" r="3.5" fill="none" stroke="#fff" stroke-width="1.5"/><path d="M14.5 8v4.5c0 2 3 2 3-1a6.5 6.5 0 1 0-3 5.5" fill="none" stroke="#fff" stroke-width="1.5"/></svg>
    <div class="box mail-list" style="left:209px;top:476px;width:174px">mix@leafio.com</div>
  </section>
</div>
</body>
</html>
```